we are plumbers and builders.

one side with kestrel fittings mark henley 07812345670 01632960418 info@kestrelfittings.co.uk
other side
kestrel building
dean henley 07700900314
01632960418
info@kestrelbuilding.co.uk

i don't want your bog standard logo id like something unusual maybe shape the card. i like black and silver,

```html
<!DOCTYPE html>
<html lang="en">
<head>
<meta charset="utf-8">
<title>Kestrel Fittings &amp; Kestrel Building – Business Cards</title>
<link rel="stylesheet" href="https://fonts.googleapis.com/css2?family=Lato:wght@400;700&family=Open+Sans:wght@700&display=swap">
<style>
  :root {
    --backdrop: #cfcfcf;
    --card-black: #1c1c1d;
    --card-charcoal: #2a2a2b;
    --pattern-tone: #333334;
    --silver: #c9c9cb;
    --brand-red: #e3212b;
    --ink-white: #f2f2f2;
  }
  * { box-sizing: border-box; margin: 0; padding: 0; }
  html, body {
    width: 1200px;
    height: 675px;
    overflow: hidden;
    background: var(--backdrop);
  }
  .canvas {
    width: 1200px;
    height: 675px;
    display: flex;
    align-items: center;
    justify-content: center;
    gap: 60px;
  }
  .card {
    position: relative;
    width: 500px;
    height: 324px;
    border-radius: 22px;
    overflow: hidden;
    background: linear-gradient(100deg, var(--card-black) 0%, var(--card-charcoal) 55%, #232324 100%);
    box-shadow: 0 18px 30px rgba(0,0,0,0.28);
  }
  .card__pattern {
    position: absolute;
    inset: 0;
    background: linear-gradient(90deg, var(--pattern-tone) 0%, var(--pattern-tone) 38%, rgba(24,24,25,0.95) 52%, var(--pattern-tone) 72%, #2f2f30 100%);
    opacity: 0.85;
  }
  .card__decoration {
    position: absolute;
    left: 30px;
    top: 30px;
    width: 170px;
    height: 210px;
    border-radius: 50%;
    background: radial-gradient(circle at 50% 45%, rgba(60,60,62,0.75) 0%, rgba(50,50,52,0.4) 50%, rgba(40,40,41,0) 72%);
  }
  .card__brand {
    position: absolute;
    left: 30px;
    top: 34px;
  }

  .brand {
    display: flex;
    align-items: center;
    gap: 10px;
  }
  .brand__dot {
    width: 22px;
    height: 22px;
    border-radius: 50%;
    background: var(--brand-red);
    flex: none;
  }
  .brand__name {
    font-family: "Lato", sans-serif;
    font-weight: 400;
    font-size: 19px;
    letter-spacing: 3px;
    text-transform: uppercase;
    color: var(--silver);
    line-height: 1;
    white-space: nowrap;
  }

  .contact {
    position: absolute;
    right: 30px;
    top: 150px;
    width: 240px;
  }
  .contact__name {
    font-family: "Lato", sans-serif;
    font-weight: 700;
    font-size: 24px;
    letter-spacing: 1px;
    text-transform: uppercase;
    color: var(--brand-red);
    text-align: right;
    margin-bottom: 12px;
    white-space: nowrap;
  }
  .contact__list { list-style: none; }
  .contact__item {
    display: flex;
    align-items: center;
    gap: 8px;
    font-family: "Open Sans", sans-serif;
    font-weight: 700;
    font-size: 13px;
    color: var(--ink-white);
    line-height: 1.75;
    white-space: nowrap;
  }
  .contact__icon {
    width: 11px;
    height: 11px;
    flex: none;
  }
</style>
</head>
<body>
<main class="canvas">

  <section class="card card--fittings" aria-label="Kestrel Fittings card">
    <div class="card__pattern" role="img" aria-label="Repeating pattern of the company mark across the card"></div>
    <div class="brand card__brand">
      <span class="brand__dot"></span>
      <span class="brand__name">Kestrel Fittings</span>
    </div>
    <div class="contact">
      <p class="contact__name">Mark Henley</p>
      <ul class="contact__list">
        <li class="contact__item">
          <svg class="contact__icon" viewBox="0 0 12 12" aria-hidden="true">
            <rect x="3" y="0.5" width="6" height="11" rx="1.3" fill="var(--brand-red)"/>
            <rect x="4.2" y="2" width="3.6" height="6.5" fill="var(--card-black)"/>
          </svg>
          07812345670
        </li>
        <li class="contact__item">
          <svg class="contact__icon" viewBox="0 0 12 12" aria-hidden="true">
            <path d="M2.5 1h2l1 3-1.3 1a6 6 0 0 0 2.8 2.8l1-1.3 3 1v2a1 1 0 0 1-1 1A9.5 9.5 0 0 1 1.5 2a1 1 0 0 1 1-1z" fill="var(--brand-red)"/>
          </svg>
          01632960418
        </li>
        <li class="contact__item">
          <svg class="contact__icon" viewBox="0 0 12 12" aria-hidden="true">
            <rect x="0.5" y="2" width="11" height="8" rx="1" fill="var(--brand-red)"/>
            <path d="M1 2.8l5 3.6 5-3.6" fill="none" stroke="var(--card-black)" stroke-width="1"/>
          </svg>
          info@kestrelfittings.co.uk
        </li>
      </ul>
    </div>
  </section>

  <section class="card card--building" aria-label="Kestrel Building card">
    <div class="card__decoration" role="img" aria-label="Large faint company mark in the background"></div>
    <div class="brand card__brand">
      <span class="brand__dot"></span>
      <span class="brand__name">Kestrel Building</span>
    </div>
    <div class="contact">
      <p class="contact__name">Dean Henley</p>
      <ul class="contact__list">
        <li class="contact__item">
          <svg class="contact__icon" viewBox="0 0 12 12" aria-hidden="true">
            <rect x="3" y="0.5" width="6" height="11" rx="1.3" fill="var(--brand-red)"/>
            <rect x="4.2" y="2" width="3.6" height="6.5" fill="var(--card-black)"/>
          </svg>
          07700900314
        </li>
        <li class="contact__item">
          <svg class="contact__icon" viewBox="0 0 12 12" aria-hidden="true">
            <path d="M2.5 1h2l1 3-1.3 1a6 6 0 0 0 2.8 2.8l1-1.3 3 1v2a1 1 0 0 1-1 1A9.5 9.5 0 0 1 1.5 2a1 1 0 0 1 1-1z" fill="var(--brand-red)"/>
          </svg>
          01632960418
        </li>
        <li class="contact__item">
          <svg class="contact__icon" viewBox="0 0 12 12" aria-hidden="true">
            <rect x="0.5" y="2" width="11" height="8" rx="1" fill="var(--brand-red)"/>
            <path d="M1 2.8l5 3.6 5-3.6" fill="none" stroke="var(--card-black)" stroke-width="1"/>
          </svg>
          info@kestrelbuilding.co.uk
        </li>
      </ul>
    </div>
  </section>

</main>
</body>
</html>
```